VELQUARTH - A modern gin bottle label

Design of a bottle label in a modern fresh design. The name of the gin is "VELQUARTH Hollow Batch K7". Please take a look at the velquarth.de website. on the main page of velquarth.de you can breathe the design direction here: 1) the taste of the gin should be composed of 10 botanicals ... an important scent note. ) a distinctive flavor is spicy and fresh 3.) The filling volume is 0.5 liters 4.) the alcohol content is 43% vol. 5.) the variety is called "dry gin" 6.) velquarth stands for "energy" and "love"

Target Market(s)

Alcohol consumer

Colors

Designer to choose colors to be used in the design.

Requirements
Must have
• the velquarth corporate logo must be included, the name of the gin is "VELQUARTH Hollow Batch K7"
Nice to have
• Please use the bottles template in the appendix. (The Black Bottles) they can use the saying "DESTILLED & BOTTLED BY OLD MARROW" in small letters

```html
<!DOCTYPE html>
<html lang="en">
<head>
<meta charset="utf-8">
<title>VELQUARTH Hollow Batch K7 – Dry Gin Label</title>
<link rel="stylesheet" href="https://fonts.googleapis.com/css2?family=Michroma&family=Metal+Mania&family=Chakra+Petch:wght@500&display=swap">
<style>
  :root {
    --backdrop: #e9e7e6;
    --label: #fbfbfb;
    --ink: #1b1b1b;
    --accent: #f47a20;
  }
  html, body {
    margin: 0;
    width: 1200px;
    height: 849px;
    overflow: hidden;
    background: var(--backdrop);
  }
  .canvas {
    position: relative;
    width: 1200px;
    height: 849px;
    display: flex;
    align-items: center;
    justify-content: center;
  }
  .label {
    width: 440px;
    height: 720px;
    background: var(--label);
    border-radius: 6px;
    box-sizing: border-box;
    padding: 120px 0 80px;
    display: flex;
    flex-direction: column;
    align-items: center;
    text-align: center;
  }
  .brand {
    display: flex;
    flex-direction: column;
    align-items: center;
    gap: 12px;
  }
  .brand__mark {
    width: 22px;
    height: 22px;
    background: var(--accent);
  }
  .brand__name {
    font-family: "Michroma", sans-serif;
    font-size: 21px;
    letter-spacing: 2px;
    color: var(--ink);
  }
  .edition {
    margin-top: 34px;
    line-height: 1;
  }
  .edition__title {
    font-family: "Metal Mania", cursive;
    font-size: 58px;
    color: var(--ink);
    letter-spacing: 1px;
  }
  .edition__sub {
    font-family: "Chakra Petch", sans-serif;
    font-weight: 500;
    font-size: 26px;
    letter-spacing: 1px;
    color: var(--accent);
    margin-top: -4px;
  }
  .variety {
    margin-top: 58px;
    font-family: "Michroma", sans-serif;
    font-size: 18px;
    letter-spacing: 3px;
    color: var(--ink);
  }
  .strength {
    margin-top: 10px;
    font-family: "Chakra Petch", sans-serif;
    font-size: 10px;
    letter-spacing: 1px;
    color: var(--accent);
  }
  .volume {
    margin-top: auto;
    font-family: "Michroma", sans-serif;
    font-size: 12px;
    letter-spacing: 3px;
    color: var(--ink);
  }
</style>
</head>
<body>
  <main class="canvas">
    <section class="label">
      <div class="brand">
        <span class="brand__mark"></span>
        <span class="brand__name">VELQUARTH</span>
      </div>
      <div class="edition">
        <div class="edition__title">Hollow</div>
        <div class="edition__sub">BATCH K7</div>
      </div>
      <div class="variety">DRY GIN</div>
      <div class="strength">43% VOL</div>
      <div class="volume">0.5 L</div>
    </section>
  </main>
</body>
</html>
```